Tidal Fern Business Cards

We need something new, fun and exciting for business cards. Our current ones are just plain and we need a design that pops. We want name, position held, phone, email on the front, and a 20% discount on the back. I have also uploaded our old business cards creative to see what we are not wanting, and how boring they were and we want something jazzed up from this, cool design and catches people attention.

```html
<!DOCTYPE html>
<html lang="en">
<head>
<meta charset="utf-8">
<title>Tidal Fern Business Cards</title>
<link rel="stylesheet" href="https://fonts.googleapis.com/css2?family=Outfit:wght@400;600;700&family=Montserrat:ital,wght@1,400;1,900&display=swap">
<style>
  :root {
    --navy: #2f4a72;
    --navy-deep: #243b5e;
    --coral: #e0706c;
    --paper: #eeeeee;
    --white: #f4f4f4;
    --backdrop: #a8a8a8;
  }
  * { margin: 0; padding: 0; box-sizing: border-box; }
  html, body { width: 1200px; height: 840px; overflow: hidden; }
  body { background: var(--backdrop); position: relative; font-family: "Outfit", sans-serif; color: var(--navy); }

  .card { position: absolute; width: 502px; height: 278px; overflow: hidden; }
  .card--front { background: var(--paper); left: 77px; }
  .card--back { background: var(--navy); left: 627px; }
  .row-top { top: 117px; }
  .row-bottom { top: 452px; }

  .pattern-strip {
    position: absolute; left: 363px; top: 10px; width: 128px; height: 259px;
    background: linear-gradient(160deg, var(--coral) 0%, var(--navy) 50%, var(--coral) 100%);
  }

  .brand { position: absolute; display: flex; align-items: center; gap: 14px; }
  .brand__dot { width: 40px; height: 40px; border-radius: 50%; background: var(--coral); }
  .brand__name { font-weight: 600; font-size: 46px; line-height: 1; color: var(--navy); letter-spacing: -0.5px; }

  .person { position: absolute; }
  .person__name { font-weight: 700; font-size: 25px; line-height: 1; color: var(--navy); }
  .person__role { font-weight: 400; font-size: 15px; color: var(--navy); margin-top: 4px; }

  .contact { position: absolute; list-style: none; }
  .contact__item { display: flex; align-items: center; gap: 9px; font-size: 15.5px; height: 23px; color: var(--navy); }
  .contact__icon { width: 20px; height: 20px; flex: none; }

  .offer-art {
    position: absolute; left: 80px; top: 40px; width: 300px; height: 160px;
    border-radius: 50% 50% 45% 45%;
    background: radial-gradient(ellipse at center, var(--navy-deep) 0%, var(--navy-deep) 35%, var(--coral) 36%, var(--coral) 60%, var(--navy) 75%);
  }
  .offer-rate {
    position: absolute; left: 0; width: 100%; top: 74px; text-align: center;
    font-family: "Montserrat", sans-serif; font-style: italic; font-weight: 400;
    font-size: 44px; line-height: 1; color: transparent;
    -webkit-text-stroke: 1.6px var(--white); padding-left: 26px;
  }
  .offer-title {
    position: absolute; left: 0; width: 100%; top: 124px; text-align: center;
    font-family: "Montserrat", sans-serif; font-style: italic; font-weight: 900;
    font-size: 50px; line-height: 1; color: var(--white); padding-left: 26px;
    text-shadow: 3px 4px 6px rgba(0,0,0,0.3);
  }
  .brush-band {
    position: absolute; left: 188px; top: 176px; width: 215px; height: 56px;
    background: var(--white); border-radius: 28px 6px 28px 6px;
  }
  .offer-brand {
    position: absolute; left: 188px; top: 188px; width: 215px; text-align: center;
    font-weight: 600; font-size: 30px; line-height: 1; color: var(--navy);
  }
</style>
</head>
<body>

  <svg width="0" height="0" style="position:absolute">
    <defs>
      <symbol id="icon-phone" viewBox="0 0 20 20">
        <circle cx="10" cy="10" r="10" fill="#e0706c"/>
        <path d="M7 5.5c.6-.4 1.2-.2 1.5.4l.7 1.5c.2.5 0 1-.4 1.3l-.5.4c.5 1.1 1.3 1.9 2.4 2.4l.4-.5c.3-.4.8-.6 1.3-.4l1.5.7c.6.3.8.9.4 1.5-.6.9-1.6 1.3-2.6 1-2.7-.9-4.6-2.8-5.5-5.5-.3-1 .1-2 1-2.6z" fill="#f4f4f4"/>
      </symbol>
      <symbol id="icon-mail" viewBox="0 0 20 20">
        <circle cx="10" cy="10" r="10" fill="#e0706c"/>
        <rect x="5" y="6.5" width="10" height="7" rx="1" fill="none" stroke="#f4f4f4" stroke-width="1.2"/>
        <path d="M5.4 7l4.6 3.6L14.6 7" fill="none" stroke="#f4f4f4" stroke-width="1.2"/>
      </symbol>
    </defs>
  </svg>

  <!-- Front, layout A -->
  <section class="card card--front row-top">
    <div class="brand" style="left:28px; top:44px;">
      <span class="brand__dot"></span>
      <span class="brand__name">Tidal Fern</span>
    </div>
    <div class="person" style="left:102px; top:132px;">
      <p class="person__name">Mara Quill</p>
      <p class="person__role">President</p>
    </div>
    <ul class="contact" style="left:102px; top:197px;">
      <li class="contact__item"><svg class="contact__icon"><use href="#icon-phone"/></svg>555-014-2277</li>
      <li class="contact__item"><svg class="contact__icon"><use href="#icon-mail"/></svg>mara@tidalfern.com</li>
    </ul>
    <div class="pattern-strip" role="img" aria-label="Tiled pattern of coral heart and ribbon motifs on navy squares"></div>
  </section>

  <!-- Back, top -->
  <section class="card card--back row-top">
    <div class="offer-art" role="img" aria-label="Large coral ribbon heart with halftone brush texture behind the offer"></div>
    <p class="offer-rate">%20</p>
    <p class="offer-title">DISCOUNT</p>
    <div class="brush-band" role="img" aria-label="White brush stroke"></div>
    <p class="offer-brand">Tidal Fern</p>
  </section>

  <!-- Front, layout B -->
  <section class="card card--front row-bottom">
    <div class="person" style="left:37px; top:37px;">
      <p class="person__name">Mara Quill</p>
      <p class="person__role">President</p>
    </div>
    <ul class="contact" style="left:34px; top:97px;">
      <li class="contact__item"><svg class="contact__icon"><use href="#icon-phone"/></svg>555-014-2277</li>
      <li class="contact__item"><svg class="contact__icon"><use href="#icon-mail"/></svg>mara@tidalfern.com</li>
    </ul>
    <div class="brand" style="left:31px; top:212px;">
      <span class="brand__dot" style="width:36px;height:36px;"></span>
      <span class="brand__name" style="font-size:42px;">Tidal Fern</span>
    </div>
    <div class="pattern-strip" role="img" aria-label="Tiled pattern of coral heart and ribbon motifs on navy squares"></div>
  </section>

  <!-- Back, bottom -->
  <section class="card card--back row-bottom">
    <div class="offer-art" role="img" aria-label="Large coral ribbon heart with halftone brush texture behind the offer"></div>
    <p class="offer-rate">%20</p>
    <p class="offer-title">DISCOUNT</p>
    <div class="brush-band" role="img" aria-label="White brush stroke"></div>
    <p class="offer-brand">Tidal Fern</p>
  </section>

</body>
</html>
```